Mrs Hobson

I would like an A5 size two sided flyer designed. This flyer is for handing out and pinningon notice boards. The brochure is prodominately for a male audience and I would prefer that it is not too 'busy'.

My business is complete housekeeping business targeted at fly in fly out miners in WA Australia. The business designs customised packages for the individual or household and completing all work while the person is at work. It is about making life simple for them so when they come home on their break all of the chores are completed and they don't have to do anything. Payments are made by Direct debit on a weekly or fortninghtly basis.

I am looking for bookings to start early 2013 for all areas of Perth.

10% discount on servcies if they included in a package with a regular house clean.

I would not like to see my exact wording from here just put into a design I would like the designer to add some thought to the design..

Please see below a list of my services.

House Cleaning
Regular clean
Spring clean
End of lease or moving clean

Inside
Linen washed
Clothes washed
Clothes ironed
Breakfast basket (Continental)
Breakfast basket (Deluxe)
Dishwashing/drying
Wheelie bins put out and in
Wheelie bins cleaned
Mail collected
Drinks stacked in fridge
Garage cleaned
Windows cleaned
Fridge Cleaned
Oven cleaned
Cupboards cleaned and organised
Carpets steam cleaned
Plants watered

Outside
Lawns mowed
Edges trimmed
Extra garden services
Windows washed
Cobwebs removed
Gutters cleaned
Reticulation maintenance/repairs
Patio area cleaned
Lawn and garden fertilising
Rubbish removal

Other
Alcohol delivery
Meet tradesperson/suppliers
Grocery shopping+
Run errands+
Bills paid+
Send or collect parcels+
Dry cleaning dropped off+
Clothing repairs alterations
Present shopping wrapping, card selection+

Your car
Car washed and vacuumed
Car detailed
Car drop off and collected for service and/or repairs+

Prodominately males and Miners

Shopping

```html
<!DOCTYPE html>
<html lang="en">
<head>
<meta charset="utf-8">
<title>Mrs Hobson – Flyer</title>
<link rel="stylesheet" href="https://fonts.googleapis.com/css2?family=Arimo:wght@400;700&family=Open+Sans:wght@400&family=Cinzel:wght@600&display=swap">
<style>
  :root {
    --brand-red: #e31b23;
    --deep-red: #8e0a10;
    --mid-red: #c8121a;
    --ink: #111111;
    --white: #ffffff;
    --yellow: #ffee00;
    --heading-yellow: #ffd21a;
    --label-grey: #e6e6e6;
  }
  * { margin: 0; padding: 0; box-sizing: border-box; }
  html, body { width: 1200px; height: 848px; overflow: hidden; background: var(--white); }
  .flyer { position: relative; width: 1200px; height: 848px; font-family: "Arimo", Arial, sans-serif; }

  /* Front side */
  .front { position: absolute; left: 0; top: 0; width: 600px; height: 848px; background: var(--white); overflow: hidden; }
  .side-label { position: absolute; top: 20px; font-family: "Arimo", Arial, sans-serif; font-weight: 700; font-size: 36px; }
  .front .side-label { left: 404px; color: var(--ink); }
  .brand { position: absolute; left: 70px; top: 112px; display: flex; align-items: center; gap: 14px; }
  .brand-dot { width: 26px; height: 26px; border-radius: 50%; background: var(--brand-red); }
  .brand-name { font-family: "Arimo", Arial, sans-serif; font-weight: 700; font-size: 82px; color: var(--brand-red); letter-spacing: -1px; }
  .cleans { position: absolute; left: 0; top: 316px; width: 600px; list-style: none; text-align: center; }
  .cleans li { font-family: "Cinzel", serif; font-weight: 600; font-size: 25px; line-height: 39px; letter-spacing: 2px; color: var(--ink); text-transform: uppercase; }
  .owner { position: absolute; left: 242px; top: 550px; font-size: 37px; color: var(--ink); }
  .swoosh { position: absolute; left: 0; top: 0; }
  .contact { position: absolute; left: 180px; top: 654px; width: 420px; text-align: center; color: var(--yellow); font-weight: 700; font-size: 26px; line-height: 33px; }

  /* Back side */
  .back { position: absolute; left: 600px; top: 0; width: 600px; height: 848px; overflow: hidden;
    background: linear-gradient(90deg, var(--deep-red) 0%, var(--mid-red) 45%, var(--brand-red) 100%); }
  .back .side-label { right: 28px; color: var(--label-grey); }
  .services-banner { position: absolute; left: 12px; top: 64px; width: 576px; height: 56px; border-radius: 28px;
    background: var(--yellow); border: 3px solid var(--white); text-align: center;
    font-weight: 700; font-size: 36px; line-height: 50px; color: var(--brand-red); }
  .service-group { position: absolute; font-family: "Open Sans", Arial, sans-serif; color: var(--white); }
  .service-group h2 { font-weight: 400; font-size: 22px; line-height: 26px; color: var(--heading-yellow); }
  .service-group ul { list-style: none; }
  .service-group li { font-size: 15.5px; line-height: 20.6px; }
  .service-group li.indent { padding-left: 30px; }
  .inside { left: 58px; top: 134px; }
  .outside { left: 325px; top: 134px; }
  .other { left: 58px; top: 536px; }
  .car { left: 325px; top: 536px; }
  .tagline { position: absolute; left: 0; top: 795px; width: 606px; text-align: center;
    font-family: "Open Sans", Arial, sans-serif; font-size: 20px; color: var(--heading-yellow); }
</style>
</head>
<body>
<main class="flyer">
  <section class="front">
    <div class="side-label">FRONT</div>
    <div class="brand">
      <span class="brand-dot"></span>
      <span class="brand-name">Mrs Hobson</span>
    </div>
    <ul class="cleans">
      <li>House Cleaning</li>
      <li>Regular Clean</li>
      <li>Spring Clean</li>
      <li>End of Lease or Moving Clean</li>
    </ul>
    <div class="owner">Dana Whitlock</div>
    <svg class="swoosh" width="600" height="848" viewBox="0 0 600 848" aria-hidden="true">
      <path d="M0,848 L0,672 C160,620 400,590 600,594 L600,848 Z" fill="var(--brand-red)"/>
      <path d="M0,738 C110,700 220,688 305,690 C220,702 110,728 0,766 Z" fill="var(--white)"/>
    </svg>
    <div class="contact">
      Call 08 6100 2875 or<br>
      0412 730 164<br>
      enquiries@mrshobson.com.au<br>
      www.mrshobson.com.au
    </div>
  </section>

  <section class="back">
    <div class="side-label">BACK</div>
    <div class="services-banner">SERVICES OFFERED</div>

    <div class="service-group inside">
      <h2>Inside</h2>
      <ul>
        <li>Linen washed</li>
        <li>Clothes washed</li>
        <li>Clothes ironed</li>
        <li>Breakfast basket (Continental)</li>
        <li>Breakfast basket (Deluxe)</li>
        <li>Dishwashing/drying</li>
        <li>Wheelie bins put out and in</li>
        <li>Wheelie bins cleaned</li>
        <li>Mail collected</li>
        <li>Drinks stacked in fridge</li>
        <li>Garage cleaned</li>
        <li>Windows cleaned</li>
        <li>Fridge Cleaned</li>
        <li>Oven cleaned</li>
        <li>Cupboards cleaned and organised</li>
        <li>Carpets steam cleaned</li>
        <li>Plants watered</li>
      </ul>
    </div>

    <div class="service-group outside">
      <h2>Outside</h2>
      <ul>
        <li>Lawns mowed</li>
        <li>Edges trimmed</li>
        <li>Extra garden services</li>
        <li>Windows washed</li>
        <li>Cobwebs removed</li>
        <li>Gutters cleaned</li>
        <li>Reticulation maintenance/repairs</li>
        <li>Patio area cleaned</li>
        <li>Lawn and garden fertilising</li>
        <li>Rubbish removal</li>
      </ul>
    </div>

    <div class="service-group other">
      <h2>Other</h2>
      <ul>
        <li>Alcohol delivery</li>
        <li>Meet tradesperson/suppliers</li>
        <li>Grocery shopping+</li>
        <li>Run errands+</li>
        <li>Bills paid+</li>
        <li>Send or collect parcels+</li>
        <li>Dry cleaning dropped off+</li>
        <li>Clothing repairs alterations</li>
        <li>Present shopping wrapping, card selection+</li>
      </ul>
    </div>

    <div class="service-group car">
      <h2>Your car</h2>
      <ul>
        <li>Car washed and vacuumed</li>
        <li>Car detailed</li>
        <li>Car drop off and collected</li>
        <li class="indent">for service and/or repairs+</li>
      </ul>
    </div>

    <div class="tagline">Mrs Hobson Doin’ your home Satisfaction Guaranteed</div>
  </section>
</main>
</body>
</html>
```